BBQ Catering & Pop-up Restaurant

I'm a catering company and a pop-up restaurant and need a website that will have the following at minimum (I'm open to suggestions): about me section, menu section, events section, a pre-order page. Here is an example of a site that I really like ... https://hollowcreeksmokehouse.example/ . I want to have a pre-order page where people can place orders online and the ability to take credit card payments. I've included a word doc with a draft write up to get started.
Updates

Reason: I am awaiting feedback from my partner and will be in touch ASAP.

Target Market(s)

BBQ Lovers

Industry/Entity Type

Caterer

Font styles to use
Serif
Other font styles liked:
• we can use multiple fonts where appropriate. I also like a faded, woody type font - which reminds me of the old western movies

Colors

Designer to choose colors to be used in the design.

Requirements
Must have
• I want
• - a smokey, woody, bbq type feel to the site.
• - my logo to be utilized
• - colors I like should compliment the colors in my logo
• - link to sign up for a news letter/ mailing list and something on the back end to capture data
Nice to have
• NA
Should not have
• NA

```html
<!DOCTYPE html>
<html lang="en">
<head>
<meta charset="utf-8">
<title>Emberline Smokehouse B.B.Q</title>
<link rel="stylesheet" href="https://fonts.googleapis.com/css2?family=Raleway:wght@300;400;500;600;700;800&family=Cormorant+Garamond:ital,wght@0,400;0,600;1,400;1,600&display=swap">
<style>
:root{
  --ember:#c8360f;
  --ember-dark:#a82b0b;
  --ink:#222;
  --muted:#666;
  --soft:#f4f4f4;
  --line:#e3e3e3;
  --night:#1f1f1f;
  --white:#fff;
  --sans:'Raleway', sans-serif;
  --serif:'Cormorant Garamond', serif;
}
*{box-sizing:border-box;margin:0;padding:0}
html,body{width:1200px;height:2936px;overflow:hidden}
body{font-family:var(--serif);color:var(--ink);background:var(--white);position:relative}
section,header,footer{position:absolute;left:0;width:1200px}

/* Hero */
.hero{top:0;height:538px;background:radial-gradient(ellipse at 50% 40%,#3a2a22 0%,#1d1512 60%,#0f0b09 100%)}
.nav{position:absolute;top:24px;left:0;width:1200px;height:40px}
.nav a{position:absolute;top:10px;font-family:var(--sans);font-weight:700;font-size:10px;letter-spacing:.5px;color:var(--white);text-decoration:none;text-transform:uppercase}
.brand{position:absolute;left:540px;top:0;width:120px;height:40px;display:flex;align-items:center;justify-content:center;gap:6px}
.brand-dot{width:10px;height:10px;border-radius:50%;background:var(--ember)}
.brand-name{font-family:var(--sans);font-weight:800;font-size:15px;color:var(--white);letter-spacing:1px}
.btn-pre{position:absolute;left:1032px;top:0;width:100px;height:22px;border-radius:11px;background:var(--ember);color:var(--white);font-family:var(--sans);font-weight:700;font-size:9px;display:flex;align-items:center;justify-content:center;letter-spacing:.5px}
.hero-title{position:absolute;top:188px;left:0;width:1200px;text-align:center;color:var(--white);font-family:var(--sans)}
.hero-title .t1{font-weight:300;font-size:40px;letter-spacing:6px;line-height:48px}
.hero-title .t2{font-weight:700;font-size:64px;letter-spacing:6px;line-height:72px;display:inline-block;border-top:1px solid rgba(255,255,255,.6);border-bottom:1px solid rgba(255,255,255,.6);padding:0 4px}
.hero-title .t3{font-weight:300;font-size:36px;letter-spacing:7px;line-height:48px}

/* Headings */
.sec-head{text-align:center;font-family:var(--sans);font-weight:400;font-size:24px;letter-spacing:.5px;color:var(--ink)}
.sec-rule{display:flex;justify-content:center;align-items:center;gap:10px;margin-top:10px}
.sec-rule span{width:48px;height:1px;background:var(--line)}
.sec-rule i{width:14px;height:8px;border:1.5px solid var(--ember);border-bottom-width:2px;border-radius:8px 8px 0 0}
.lead{font-style:italic;font-size:13.5px;color:var(--muted);text-align:center;line-height:18px}

/* About */
.about{top:538px;height:529px}
.about .sec-head{margin-top:56px}
.about .lead{width:460px;margin:22px auto 0}
.menu-note{position:absolute;width:220px}
.menu-note h4{font-style:italic;font-weight:600;font-size:13px;text-transform:uppercase;letter-spacing:.5px}
.menu-note p{font-style:italic;font-size:12.5px;color:var(--muted);line-height:16px;margin-top:6px}
.menu-note.right{text-align:right}
.menu-note.divided{border-bottom:1px solid var(--line);padding-bottom:14px}
.call{position:absolute;left:499px;top:218px;width:196px;height:196px;border-radius:50%;background:var(--ember);color:var(--white);text-align:center;font-family:var(--sans)}
.call .lbl{margin-top:56px;font-weight:700;font-size:14px}
.call .num{font-weight:600;font-size:14px;margin-top:4px}
.dish{position:absolute;border-radius:50%}

/* Menu tiles */
.menu{top:1067px;height:250px;display:flex}
.tile{flex:1;position:relative;display:flex;flex-direction:column;align-items:center;justify-content:center}
.tile h3{font-style:italic;font-weight:400;font-size:20px;color:var(--white);letter-spacing:1px;text-transform:uppercase;display:flex;align-items:center;gap:14px}
.tile h3::before,.tile h3::after{content:"";width:44px;height:1px;background:rgba(255,255,255,.6)}
.tile .view{margin-top:10px;width:66px;height:18px;border-radius:9px;border:1px solid var(--white);color:var(--white);font-family:var(--sans);font-size:7px;font-weight:700;display:flex;align-items:center;justify-content:center}
.tile .view.on{background:var(--ember);border-color:var(--ember)}

/* Booking */
.book{top:1317px;height:259px;background:var(--soft)}
.book .sec-head{margin-top:60px}
.book .lead{margin-top:14px;font-size:12px}
.book .lead b{color:var(--ember);font-weight:400}
.book-form{position:absolute;top:174px;left:235px;width:730px;height:26px;display:flex;gap:32px}
.field{width:168px;height:26px;background:var(--white);border:1px solid var(--line);display:flex;align-items:center;justify-content:space-between;padding:0 8px;font-style:italic;font-size:11px;color:#888}
.field svg{width:11px;height:11px}
.btn-book{flex:1;height:26px;border-radius:13px;background:var(--ember);color:var(--white);font-family:var(--sans);font-weight:700;font-size:9px;display:flex;align-items:center;justify-content:center;letter-spacing:.5px}

/* Events */
.events{top:1576px;height:530px}
.events .sec-head{margin-top:60px}
.events .lead{margin-top:20px;font-size:12.5px}
.cards{position:absolute;top:172px;left:235px;width:730px;display:flex;gap:20px}
.card{width:230px}
.card .photo{height:156px;position:relative}
.card .photo::after{content:"";position:absolute;inset:8px;border:1px solid rgba(255,255,255,.6)}
.card .meta{margin-top:18px;font-style:italic;font-size:9.5px;color:var(--muted);border-left:2px solid var(--line);padding-left:8px}
.card .meta b{color:var(--ember);font-weight:400}
.card h5{font-style:italic;font-weight:600;font-size:12.5px;text-transform:uppercase;margin:6px 0 0 10px}
.card p{font-style:italic;font-size:10.5px;color:var(--muted);line-height:14px;margin:12px 0 0 10px}
.card .more{display:block;font-style:italic;font-size:10.5px;color:var(--ember);margin:12px 0 0 10px}

/* Gallery + preorder */
.gallery{top:2106px;height:164px;display:flex}
.gallery div{flex:1}
.preorder{top:2270px;height:45px;background:var(--ember);color:var(--white);display:flex;align-items:center;justify-content:center;gap:18px;font-family:var(--sans);font-size:17px;letter-spacing:.5px}
.map{top:2315px;height:313px;background:linear-gradient(135deg,#ecebe6 0%,#e4e6df 60%,#dfe6da 100%)}
.pin{position:absolute;left:566px;top:110px}

/* Footer */
.site-footer{top:2628px;height:308px;background:var(--night);color:#bbb}
.pizza{position:absolute;left:-60px;top:42px;width:176px;height:176px;border-radius:50%;background:radial-gradient(circle,#d9a24a 0%,#c2572b 60%,#8e3a1d 100%)}
.socials{position:absolute;top:41px;left:0;width:1200px;display:flex;justify-content:center;gap:14px}
.socials span{width:24px;height:24px;border-radius:50%;background:var(--white)}
.socials span:first-child{background:var(--ember)}
.foot-brand{position:absolute;top:90px;left:0;width:1200px;display:flex;justify-content:center;align-items:center;gap:8px}
.foot-brand .brand-name{font-size:20px}
.foot-cols{position:absolute;top:166px;left:220px;width:760px;height:78px;border-top:1px solid #3a3a3a;display:flex}
.foot-col{flex:1;text-align:center;padding-top:22px}
.foot-col+.foot-col{border-left:1px solid #3a3a3a}
.foot-col h6{font-style:italic;font-weight:600;font-size:13px;color:#ddd}
.foot-col p{font-family:var(--sans);font-size:8.5px;margin-top:10px;color:#999}
.copy{position:absolute;top:272px;left:0;width:1200px;text-align:center;font-family:var(--sans);font-size:8.5px;color:#888}
</style>
</head>
<body>

<header class="hero" role="img" aria-label="Dark photograph of meat and vegetables grilling over a barbecue">
  <nav class="nav">
    <a style="left:415px">Home</a>
    <a style="left:462px">The Menu</a>
    <div class="brand"><span class="brand-dot"></span><span class="brand-name">EMBERLINE</span></div>
    <a style="left:680px">About Miles</a>
    <a style="left:760px">Our Shop</a>
    <div class="btn-pre">PREORDER</div>
  </nav>
  <div class="hero-title">
    <div class="t1">EMBERLINE</div>
    <div class="t2">SMOKEHOSE</div>
    <div class="t3">B.B.Q</div>
  </div>
</header>

<section class="about">
  <h2 class="sec-head">ABOUT EMBERLINE</h2>
  <div class="sec-rule"><span></span><i></i><span></span></div>
  <p class="lead">Slow smoked over oak for hours, our brisket, ribs and sausage come straight from the pit to your table. We cater weddings, parties and pop-up nights across town, and every plate is cooked low and slow with care.</p>

  <div class="menu-note divided" style="left:235px;top:224px">
    <h4>• Dessert</h4>
    <p>Peach cobbler and banana pudding, made fresh every morning in house.</p>
  </div>
  <div class="menu-note" style="left:235px;top:314px">
    <h4>• Breakfast</h4>
    <p>Brisket tacos and biscuits served hot until the pit runs out.</p>
  </div>
  <div class="dish" role="img" aria-label="Skewers of grilled meat" style="left:230px;top:395px;width:120px;height:50px;border-radius:25px;background:linear-gradient(90deg,#8a3a1a,#b3582a,#6e2c14)"></div>

  <div class="call">
    <div class="lbl">CALL US NOW</div>
    <div class="num">(555) 014-2290</div>
  </div>
  <div class="dish" role="img" aria-label="Plate of fried chicken with dipping sauce" style="left:502px;top:340px;width:170px;height:84px;border-radius:50%;background:radial-gradient(ellipse,#c98a3c 0%,#a65a22 55%,#f2f2f2 75%)"></div>

  <div class="dish" role="img" aria-label="Single grilled skewer" style="left:900px;top:200px;width:30px;height:80px;border-radius:14px;background:linear-gradient(180deg,#7a2f14,#b15a2c)"></div>
  <div class="menu-note right divided" style="left:745px;top:298px">
    <h4>Lunch •</h4>
    <p>Chopped beef sandwiches, pulled pork plates and smoky sides daily.</p>
  </div>
  <div class="menu-note right" style="left:745px;top:406px">
    <h4>Drinks •</h4>
    <p>Sweet tea, lemonade and cold local beer.</p>
  </div>
</section>

<section class="menu">
  <div class="tile" role="img" aria-label="Breakfast burger on a plate" style="background:linear-gradient(160deg,#4a3a30,#2b211c)"><h3>Breakfast</h3><span class="view on">VIEW MORE</span></div>
  <div class="tile" role="img" aria-label="Meat skewers on a grill" style="background:linear-gradient(160deg,#6a4a34,#3b2a20)"><h3>Lunch</h3><span class="view">VIEW MORE</span></div>
  <div class="tile" role="img" aria-label="Dinner plates on a wooden table" style="background:linear-gradient(160deg,#4b3a2c,#2a201a)"><h3>Dinner</h3><span class="view">VIEW MORE</span></div>
  <div class="tile" role="img" aria-label="Glasses of drinks on a table" style="background:linear-gradient(160deg,#5a4a3e,#3a2e26)"><h3>Drinks</h3><span class="view">VIEW MORE</span></div>
</section>

<section class="book">
  <h2 class="sec-head">BOOK A TABLE</h2>
  <div class="sec-rule"><span></span><i></i><span></span></div>
  <p class="lead">You can call us directly at: <b>+1 (555) 014 7788</b></p>
  <div class="book-form">
    <div class="field">Date *<svg viewBox="0 0 12 12"><rect x="1" y="2" width="10" height="9" fill="none" stroke="#999"/><line x1="1" y1="5" x2="11" y2="5" stroke="#999"/></svg></div>
    <div class="field">Time *<svg viewBox="0 0 12 12"><circle cx="6" cy="6" r="5" fill="none" stroke="#999"/><path d="M6 3v3h2" fill="none" stroke="#999"/></svg></div>
    <div class="field">Seat *<svg viewBox="0 0 12 12"><circle cx="4" cy="4" r="2" fill="#999"/><circle cx="8" cy="4" r="2" fill="#999"/><path d="M1 11c0-3 6-3 6 0M5 11c0-3 6-3 6 0" fill="#999"/></svg></div>
    <div class="btn-book">BOOK A TABLE</div>
  </div>
</section>

<section class="events">
  <h2 class="sec-head">OUR EVENTS</h2>
  <div class="sec-rule"><span></span><i></i><span></span></div>
  <p class="lead">Join us for pop-up suppers, pit nights and summer cookouts. Follow along to hear about our next event first.</p>
  <div class="cards">
    <article class="card">
      <div class="photo" role="img" aria-label="Chef working in a kitchen" style="background:linear-gradient(160deg,#5d6f80,#232a33)"></div>
      <div class="meta">Posted by <b>Admin</b> &nbsp;/&nbsp; March 9, 2017 &nbsp;/&nbsp; <b>4 Comments</b></div>
      <h5>Summer Vacation Ideas</h5>
      <p>Warm nights, cold drinks and a pit full of ribs. Plan your summer party with our team today.</p>
      <span class="more">View More</span>
    </article>
    <article class="card">
      <div class="photo" role="img" aria-label="Restaurant interior with tables" style="background:linear-gradient(160deg,#6e5b48,#2f2620)"></div>
      <div class="meta">Posted by <b>Admin</b> &nbsp;/&nbsp; March 9, 2017 &nbsp;/&nbsp; <b>4 Comments</b></div>
      <h5>Summer Vacation Ideas</h5>
      <p>Warm nights, cold drinks and a pit full of ribs. Plan your summer party with our team today.</p>
      <span class="more">View More</span>
    </article>
    <article class="card">
      <div class="photo" role="img" aria-label="Plated steak dish on a white table" style="background:linear-gradient(160deg,#f0eeea,#c9bfb4)"></div>
      <div class="meta">Posted by <b>Admin</b> &nbsp;/&nbsp; March 9, 2017 &nbsp;/&nbsp; <b>4 Comments</b></div>
      <h5>Summer Vacation Ideas</h5>
      <p>Warm nights, cold drinks and a pit full of ribs. Plan your summer party with our team today.</p>
      <span class="more">View More</span>
    </article>
  </div>
</section>

<section class="gallery">
  <div role="img" aria-label="Set dining tables with glasses" style="background:linear-gradient(160deg,#6c747a,#2c3034)"></div>
  <div role="img" aria-label="Bowls of spices on a table" style="background:linear-gradient(160deg,#7a5636,#3a2a1c)"></div>
  <div role="img" aria-label="Chef plating a dish" style="background:linear-gradient(160deg,#8a6a4e,#3e2e22)"></div>
  <div role="img" aria-label="Wine bottles on a shelf" style="background:linear-gradient(160deg,#4a3a34,#1e1715)"></div>
  <div role="img" aria-label="Cook working at a kitchen counter" style="background:linear-gradient(160deg,#8c7a66,#4a3a2e)"></div>
  <div role="img" aria-label="Plates of food on a table" style="background:linear-gradient(160deg,#7a5a44,#3a2a20)"></div>
</section>

<section class="preorder">PREORDER NOW <span>→</span></section>

<section class="map" role="img" aria-label="Street map showing the restaurant location">
  <svg class="pin" width="26" height="36" viewBox="0 0 26 36"><path d="M13 0C6 0 0 6 0 13c0 9 13 23 13 23s13-14 13-23C26 6 20 0 13 0z" fill="#d3382b"/><circle cx="13" cy="13" r="5" fill="#fff"/></svg>
</section>

<footer class="site-footer">
  <div class="pizza" role="img" aria-label="Pizza seen from above"></div>
  <div class="socials" aria-label="Social links"><span></span><span></span><span></span><span></span></div>
  <div class="foot-brand"><span class="brand-dot"></span><span class="brand-name">EMBERLINE</span></div>
  <div class="foot-cols">
    <div class="foot-col"><h6>Address:</h6><p>410 Cedar Row, Oakvale 70100</p></div>
    <div class="foot-col"><h6>Reservation Online:</h6><p>(555) 014-2290</p></div>
    <div class="foot-col"><h6>Timming:</h6><p>Mondays Closed &nbsp;&nbsp; Tues-Sun 11AM-Sold Out</p></div>
  </div>
  <div class="copy">© 2017 Emberline Smokehouse</div>
</footer>

</body>
</html>
```